Fieldstone Sporting
F.S.S. Sports
Project: Fieldstone Sporting
Fieldstone Sporting - Sports
Creative Brief
Use same font as used in my logo
Use your better judgement
Professional
Weston L. Barrow Jr.
CEO
Larkhaven, QX
W.barrow@quillmail.example
www.FSSsports.example
Logo and web address
Concepts
Business card and stationary design. We provide umpires & referees for teams/organizations.

```html
<!DOCTYPE html>
<html lang="en">
<head>
<meta charset="utf-8">
<title>Fieldstone Sporting Stationery</title>
<link href="https://fonts.googleapis.com/css2?family=Montserrat:wght@400;600;800&display=swap" rel="stylesheet">
<style>
  :root {
    --stage: #a8a9ab;
    --paper: #ffffff;
    --navy: #1f3c78;
    --green: #7cc142;
    --ink: #4a4a4a;
    --muted: #8a8a8a;
    --fold: #d6d6d6;
    --shade: rgba(0,0,0,0.18);
  }
  * { box-sizing: border-box; margin: 0; padding: 0; }
  html, body { width: 1200px; height: 626px; overflow: hidden; }
  body {
    background: var(--stage);
    font-family: "Montserrat", Arial, sans-serif;
    position: relative;
  }
  .sheet {
    position: absolute;
    background: var(--paper);
    box-shadow: 0 1px 3px var(--shade);
    overflow: hidden;
  }
  .brand {
    display: flex; align-items: center; justify-content: center; gap: 6px;
    color: var(--navy); font-weight: 800; letter-spacing: 0.02em;
    white-space: nowrap;
  }
  .brand-dot { border-radius: 50%; background: var(--green); flex: none; }
  .edge-bands { position: absolute; left: 0; right: 0; bottom: 0; }
  .edge-bands .blue { height: 2px; background: var(--navy); }
  .edge-bands .green { background: var(--green); }
  .tiny { font-size: 5px; color: var(--muted); text-align: center; white-space: nowrap; }

  /* business card front */
  .card-front { left: 34px; top: 197px; width: 177px; height: 101px; border-radius: 6px; }
  .card-front .brand { position: absolute; top: 42px; left: 0; right: 0; font-size: 11px; }
  .card-front .brand-dot { width: 8px; height: 8px; }
  .card-front .web { position: absolute; top: 80px; left: 0; right: 0; }
  .card-front .edge-bands .green { height: 4px; }

  /* business card back */
  .card-back { left: 34px; top: 312px; width: 177px; height: 101px; border-radius: 6px; }
  .card-back .brand { position: absolute; top: 14px; left: 0; right: 0; font-size: 8px; }
  .card-back .brand-dot { width: 6px; height: 6px; }
  .card-back .person { position: absolute; top: 56px; left: 0; right: 0; text-align: center; font-size: 6px; color: var(--ink); font-weight: 600; }
  .card-back .contact { position: absolute; top: 74px; left: 0; right: 0; line-height: 7px; font-size: 4.5px; }
  .card-back .edge-bands .green { height: 4px; }

  /* letterhead */
  .letterhead { left: 233px; top: 29px; width: 360px; height: 566px; }
  .letterhead .brand { position: absolute; top: 44px; left: 0; right: 0; font-size: 16px; }
  .letterhead .brand-dot { width: 12px; height: 12px; }
  .letterhead .web { position: absolute; top: 523px; left: 0; right: 0; font-size: 5.5px; }
  .letterhead .contact { position: absolute; top: 538px; left: 0; right: 0; }
  .letterhead .edge-bands .green { height: 10px; }

  /* envelope back */
  .envelope-back { left: 682px; top: 74px; width: 487px; height: 231px; }
  .envelope-back .flap { position: absolute; inset: 0; }
  .envelope-back .motif {
    position: absolute; left: 222px; top: 22px; width: 44px; height: 38px;
    border-radius: 4px; background: linear-gradient(135deg, #3b5b8f, #9aa6ba);
    opacity: 0.7;
  }

  /* envelope front */
  .envelope-front { left: 682px; top: 336px; width: 487px; height: 209px; }
  .envelope-front .brand { position: absolute; top: 46px; left: 0; right: 0; font-size: 15px; }
  .envelope-front .brand-dot { width: 11px; height: 11px; }
  .envelope-front .web { position: absolute; top: 168px; left: 0; right: 0; }
  .envelope-front .contact { position: absolute; top: 177px; left: 0; right: 0; }
  .envelope-front .edge-bands { bottom: 14px; }
  .envelope-front .edge-bands .green { height: 2px; margin-top: 2px; }
</style>
</head>
<body>

<section class="sheet card-front">
  <div class="brand"><span class="brand-dot"></span>Fieldstone Sporting</div>
  <p class="tiny web">www.FSSsports.example</p>
  <div class="edge-bands"><div class="blue"></div><div class="green"></div></div>
</section>

<section class="sheet card-back">
  <div class="brand"><span class="brand-dot"></span>Fieldstone Sporting</div>
  <p class="person">Weston L. Barrow Jr., CEO</p>
  <div class="tiny contact">
    Larkhaven, QX | Phone: 000 555 0142 | Cell: 000 555 0178<br>
    W.barrow@quillmail.example
  </div>
  <div class="edge-bands"><div class="blue"></div><div class="green"></div></div>
</section>

<section class="sheet letterhead">
  <div class="brand"><span class="brand-dot"></span>Fieldstone Sporting</div>
  <p class="tiny web">www.FSSsports.example</p>
  <p class="tiny contact">Larkhaven, QX | Phone: 000 555 0142 | Cell: 000 555 0178 | Email: W.barrow@quillmail.example</p>
  <div class="edge-bands"><div class="blue"></div><div class="green"></div></div>
</section>

<section class="sheet envelope-back">
  <svg class="flap" viewBox="0 0 487 231" preserveAspectRatio="none">
    <polyline points="0,0 243.5,95 487,0" fill="none" stroke="#d6d6d6" stroke-width="1"/>
  </svg>
  <div class="motif" role="img" aria-label="Small illustration of a running athlete"></div>
</section>

<section class="sheet envelope-front">
  <div class="brand"><span class="brand-dot"></span>Fieldstone Sporting</div>
  <p class="tiny web">www.FSSsports.example</p>
  <p class="tiny contact">Larkhaven, QX | Phone: 000 555 0142 | Cell: 000 555 0178 | Email: W.barrow@quillmail.example</p>
  <div class="edge-bands"><div class="blue"></div><div class="green"></div></div>
</section>

</body>
</html>
```